Labour Hire Co. Billboard Design

We have a billboard (pic attached in the brief) that we want a design for our other company..

The company - RBV supplies trades to the mining, maintenance, fabrication and construction industries.
People drive by this billboard at speed 80kmh, so an obvious, in your face, simple message and graphics are essential - including a large logo so it can be seen from a distance.

Target Market(s)

Managers of heavy industrial companies. Note, we are not using this billboard to target candidates / employees. Our audience for this billboard is managers and executives. Our aim is brand recognition.

Industry/Entity Type

Construction

Font styles to use
Sans Serif

Colors
faed33
fffefd
0692cd

Requirements
Must have
• Simplicity
• Eye Catching
• Credible
• Consistent with our brand - See www.rbvqn.com.au
• Note, only the top 2/3rds of the billboard is viewable so take this into account with the design. The logo should really be the website inside the design of our logo, i.e. the same graphic as our logo, but quoting the website.
• Tag line could be "Quality tradespeople - quickly and safely" Please feel free to come up with alternatives. We are open to ideas though.
Nice to have
• See the images attached, previously we have tried to be clever with this billboard, i.e. man climbing up the roof, etc.
• Perhaps here we could have a tradesperson on a worksite/ minesite repairing the top of the billboard so it blends cleverly into the landscape. But skip this step if it takes away from the effect of the billboard.
Should not have
• Too wordy, or small so it cannot be worked out in 2 seconds of looking at it.
• Colours other than our our corporate colours.

```html
<!DOCTYPE html>
<html lang="en">
<head>
<meta charset="utf-8">
<title>RBV Billboard – Quality Trades People</title>
<link rel="stylesheet" href="https://fonts.googleapis.com/css2?family=Arimo:wght@400&family=Roboto+Condensed:wght@700&display=swap">
<style>
  :root {
    --brand-blue: #0692cd;
    --brand-yellow: #faed33;
    --badge-yellow: #fdc010;
    --charcoal: #4a4a4c;
    --white: #fffefd;
    --worker-dark: #231f20;
  }
  html, body {
    margin: 0;
    padding: 0;
    overflow: hidden;
    background: var(--white);
  }
  .billboard {
    position: relative;
    width: 1200px;
    height: 771px;
    overflow: hidden;
    background: var(--white);
    font-family: "Arimo", Arial, sans-serif;
  }
  .billboard__band {
    position: absolute;
    inset: 0;
    width: 1200px;
    height: 771px;
  }
  .billboard__rule {
    position: absolute;
    left: 74px;
    top: 40px;
    width: 3px;
    height: 662px;
    background: var(--brand-blue);
  }
  .worker-figure {
    position: absolute;
    left: 722px;
    top: 135px;
    width: 290px;
    height: 610px;
    border-radius: 120px 120px 36px 36px;
    background: linear-gradient(165deg, var(--badge-yellow) 0%, var(--badge-yellow) 22%, var(--worker-dark) 42%, var(--worker-dark) 100%);
  }
  .headline,
  .tagline,
  .phone {
    position: absolute;
    margin: 0;
    line-height: 1;
    white-space: nowrap;
    font-weight: 400;
  }
  .headline--quality {
    left: 106px;
    top: 14px;
    font-size: 158px;
    letter-spacing: -10px;
    color: var(--brand-blue);
  }
  .headline--trades {
    left: 112px;
    top: 158px;
    font-family: "Roboto Condensed", "Arial Narrow", sans-serif;
    font-weight: 700;
    font-size: 90px;
    color: var(--charcoal);
  }
  .tagline {
    left: 114px;
    color: var(--white);
  }
  .tagline--quickly {
    top: 270px;
    font-size: 186px;
    letter-spacing: -8px;
  }
  .tagline--safely {
    top: 432px;
    font-size: 112px;
    letter-spacing: -4px;
  }
  .phone {
    left: 112px;
    top: 590px;
    font-size: 118px;
    letter-spacing: -10px;
    color: var(--brand-blue);
  }
  .brand-badge {
    position: absolute;
    left: 848px;
    top: 12px;
    width: 286px;
    height: 286px;
    border-radius: 50%;
    background: var(--badge-yellow);
    display: flex;
    align-items: center;
    justify-content: center;
  }
  .brand-badge__name {
    font-family: "Roboto Condensed", "Arial Narrow", sans-serif;
    font-weight: 700;
    font-size: 112px;
    color: var(--charcoal);
    line-height: 1;
  }
</style>
</head>
<body>
  <main class="billboard">
    <svg class="billboard__band" viewBox="0 0 1200 771" aria-hidden="true">
      <polygon points="0,245 1200,355 1200,640 0,522" fill="var(--brand-blue)"/>
    </svg>

    <div class="billboard__rule"></div>

    <div class="worker-figure" role="img" aria-label="Silhouette of a kneeling tradesperson in a yellow hard hat and hi-vis vest measuring with a tape"></div>

    <h1 class="headline headline--quality">QUALITY</h1>
    <h2 class="headline headline--trades">TRADES PEOPLE</h2>

    <p class="tagline tagline--quickly">Quickly</p>
    <p class="tagline tagline--safely">&amp; Safely</p>

    <p class="phone">08 6000 4271</p>

    <div class="brand-badge">
      <span class="brand-badge__name">RBV</span>
    </div>
  </main>
</body>
</html>
```